Unique Business Card Design

Unique Business Card design for our orthotic and prosthetic company. Our logo is on our website, color is light blue. Unique shape (artificial leg shaped, vertical, etc..) preferred. Logo, business name, individual name and basic demographics needed.

Industry/Entity Type

Business

Contact Information for Business Card

Logo, Industry, Phone # Logo, "Prosthetic & Orthotic Services" Place to add individual name and contact info

Colors
cee9f5

Requirements
Must have
• The icon must be there, placement of "Prosthetic & Orthotic Services" can be moved
Nice to have
• Like the mix of light blue, and a little darker blue. One design included the icons from my website which was a nice touch

```html
<!DOCTYPE html>
<html lang="en">
<head>
<meta charset="utf-8">
<title>Limbwell Inc. Business Card</title>
<link rel="stylesheet" href="https://fonts.googleapis.com/css2?family=Source+Sans+3:wght@400;600;700&family=Crimson+Text:ital@1&display=swap">
<style>
  :root {
    --stage: #3a3836;
    --card-light: #f4f3ef;
    --card-mid: #dcdad4;
    --navy: #1f3160;
    --navy-deep: #0f1838;
    --band: #2a3f7e;
    --ink: #2b3a5f;
    --text: #4a4a4a;
    --icon: #33405a;
  }
  * { margin: 0; padding: 0; box-sizing: border-box; }
  html, body { width: 1200px; height: 834px; overflow: hidden; }
  body {
    position: relative;
    background: var(--stage);
    font-family: "Source Sans 3", "Helvetica Neue", Arial, sans-serif;
  }
  .card {
    position: absolute;
    left: 293px; top: 207px;
    width: 730px; height: 414px;
    border-radius: 14px;
    overflow: hidden;
    background: radial-gradient(ellipse at 35% 45%, var(--card-light) 0%, #e9e7e2 55%, var(--card-mid) 100%);
  }
  .side-band {
    position: absolute;
    right: 0; top: 0;
    width: 92px; height: 100%;
    background: linear-gradient(90deg, var(--band), var(--navy));
  }
  .figure-art {
    position: absolute;
    left: 512px; top: 0;
    width: 196px; height: 410px;
    border-radius: 60px 60px 30px 30px;
    background: linear-gradient(180deg, var(--navy) 0%, var(--navy-deep) 100%);
    opacity: 0.92;
  }
  .brand {
    position: absolute;
    left: 39px; top: 35px;
    display: flex; align-items: center;
  }
  .brand-mark {
    width: 96px; height: 96px;
    border-radius: 50%;
    background: var(--navy);
  }
  .brand-text { margin-left: 24px; margin-top: -8px; }
  .brand-name {
    font-weight: 600;
    font-size: 27px;
    letter-spacing: 0.2px;
    color: var(--navy);
    line-height: 1;
    padding-bottom: 6px;
    border-bottom: 2px solid var(--navy);
    width: 242px;
  }
  .brand-tagline {
    font-family: "Crimson Text", Georgia, serif;
    font-style: italic;
    font-size: 16px;
    color: var(--navy);
    margin-top: 4px;
    padding-left: 14px;
  }
  .person {
    position: absolute;
    left: 38px; top: 154px;
    color: var(--ink);
    font-weight: 700;
    font-size: 23px;
  }
  .person .credentials { font-weight: 600; font-size: 17px; }
  .contacts {
    position: absolute;
    left: 40px; top: 198px;
    list-style: none;
  }
  .contacts li {
    display: flex; align-items: center;
    height: 29.3px;
    font-size: 18px;
    color: var(--text);
  }
  .contacts li.address { margin-top: 11px; }
  .contacts svg { width: 20px; height: 20px; margin-right: 10px; flex: none; }
</style>
</head>
<body>
  <div class="card">
    <div class="side-band"></div>
    <div class="figure-art" role="img" aria-label="Navy silhouette of a standing human figure"></div>

    <div class="brand">
      <div class="brand-mark"></div>
      <div class="brand-text">
        <div class="brand-name">LIMBWELL INC.</div>
        <div class="brand-tagline">Prosthetic &amp; Orthotic Services</div>
      </div>
    </div>

    <div class="person">Mira Castellan<span class="credentials">, CO LPO</span></div>

    <ul class="contacts">
      <li>
        <svg viewBox="0 0 20 20"><circle cx="10" cy="10" r="10" fill="var(--icon)"/><path d="M6.5 5.5l2 0 1 2.5-1.3 1a6 6 0 0 0 2.8 2.8l1-1.3 2.5 1v2a1.2 1.2 0 0 1-1.3 1A8.5 8.5 0 0 1 5.5 6.8a1.2 1.2 0 0 1 1-1.3z" fill="#fff"/></svg>
        555.204.1180
      </li>
      <li>
        <svg viewBox="0 0 20 20"><circle cx="10" cy="10" r="10" fill="var(--icon)"/><rect x="7" y="5" width="6" height="3" fill="#fff"/><rect x="5" y="8.5" width="10" height="4.5" rx="1" fill="#fff"/><rect x="7" y="12" width="6" height="3" fill="#fff"/></svg>
        555.204.1181
      </li>
      <li>
        <svg viewBox="0 0 20 20"><circle cx="10" cy="10" r="10" fill="var(--icon)"/><rect x="7" y="4.5" width="6" height="11" rx="1.2" fill="none" stroke="#fff" stroke-width="1.5"/><circle cx="10" cy="13.3" r="0.8" fill="#fff"/></svg>
        555-317.6242
      </li>
      <li>
        <svg viewBox="0 0 20 20"><circle cx="10" cy="10" r="10" fill="var(--icon)"/><rect x="5" y="6.5" width="10" height="7" rx="0.8" fill="#fff"/><path d="M5.3 7l4.7 3.6L14.7 7" fill="none" stroke="var(--icon)" stroke-width="1"/></svg>
        Mcastellan@limbwellinc.com
      </li>
      <li>
        <svg viewBox="0 0 20 20"><circle cx="10" cy="10" r="10" fill="var(--icon)"/><circle cx="10" cy="10" r="4.8" fill="none" stroke="#fff" stroke-width="1.4"/><path d="M5.2 10h9.6M10 5.2c-2 2.8-2 6.8 0 9.6M10 5.2c2 2.8 2 6.8 0 9.6" fill="none" stroke="#fff" stroke-width="1"/></svg>
        www.limbwellinc.com
      </li>
      <li class="address">
        <svg viewBox="0 0 20 20"><circle cx="10" cy="10" r="10" fill="var(--icon)"/><path d="M10 4.5a3.8 3.8 0 0 0-3.8 3.8c0 2.8 3.8 7 3.8 7s3.8-4.2 3.8-7A3.8 3.8 0 0 0 10 4.5z" fill="#fff"/><circle cx="10" cy="8.3" r="1.4" fill="var(--icon)"/></svg>
        2380 W. 14th St. Fairview, NY 10990
      </li>
    </ul>
  </div>
</body>
</html>
```